Laundry pickup and delivery flyer "Fold Harbor laundry"

I need a flyer "8.5"x11" that tells customers about our pickup and delivery laundry service. our website address is: www.foldharborlaundry.example The flyer should be front and back.

Font styles to use
Sans Serif

Colors
0094D4
00A9DD
6FCCEA
C7EBF8
E9F6FB

```html
<!DOCTYPE html>
<html lang="en">
<head>
<meta charset="utf-8">
<title>Fold Harbor laundry – How it works</title>
<link href="https://fonts.googleapis.com/css2?family=Montserrat:wght@800&family=Questrial&display=swap" rel="stylesheet">
<style>
  :root {
    --sky: #c9fbf9;
    --wave: #42d6f8;
    --headline: #3cb6f5;
    --copy: #3ab4f2;
    --disc: #5bd4d7;
    --disc-rim: #9ef5ea;
    --disc-shadow: #42d6f8;
    --dots: #1e4f9a;
    --bubble: #8ff4e8;
    --white: #ffffff;
  }
  html, body { margin: 0; padding: 0; overflow: hidden; }
  .flyer {
    position: relative;
    width: 928px;
    height: 1200px;
    background: var(--white);
    overflow: hidden;
    font-family: "Questrial", sans-serif;
  }
  .decor { position: absolute; inset: 0; }
  .site-url {
    position: absolute;
    right: 50px;
    top: 46px;
    margin: 0;
    font-size: 31px;
    color: var(--copy);
    letter-spacing: 0.3px;
  }
  .headline {
    position: absolute;
    left: 134px;
    top: 252px;
    margin: 0;
    font-family: "Montserrat", sans-serif;
    font-weight: 800;
    font-size: 66px;
    letter-spacing: -1px;
    color: var(--headline);
  }
  .step-text {
    position: absolute;
    margin: 0;
    font-size: 22px;
    line-height: 24px;
    color: var(--copy);
    width: 240px;
  }
  .step-1 { left: 148px; top: 615px; }
  .step-2 { left: 529px; top: 622px; }
  .step-3 { left: 150px; top: 959px; }
  .step-4 { left: 529px; top: 963px; }
  .footer-band {
    position: absolute;
    left: 0; right: 0; bottom: 0;
    height: 62px;
    background: var(--sky);
  }
</style>
</head>
<body>
<main class="flyer">
  <svg class="decor" width="928" height="1200" viewBox="0 0 928 1200">
    <!-- header wave -->
    <path d="M0 0 H928 V232 C820 262 720 262 600 225 C450 170 360 60 220 62 C120 64 50 110 0 145 Z" fill="var(--sky)"/>
    <path d="M0 145 C50 110 120 64 220 62 C360 60 450 170 600 225 C720 262 820 262 928 232"
          fill="none" stroke="var(--wave)" stroke-width="20"/>

    <!-- floating bubbles -->
    <g fill="none" stroke="var(--bubble)" stroke-width="2">
      <circle cx="87" cy="138" r="11"/>
      <circle cx="316" cy="185" r="9"/>
      <circle cx="832" cy="377" r="11"/>
      <circle cx="502" cy="900" r="12"/>
      <circle cx="851" cy="892" r="9"/>
    </g>

    <!-- dotted trails -->
    <g fill="none" stroke="var(--dots)" stroke-width="4.5" stroke-linecap="round" stroke-dasharray="0 10">
      <path d="M99 422 C100 385 130 355 234 353"/>
      <path d="M95 542 V710"/>
      <path d="M792 752 V920"/>
      <path d="M534 1101 H730 C770 1101 787 1070 787 1032"/>
    </g>

    <!-- step discs -->
    <g class="disc">
      <circle cx="247" cy="501" r="92" fill="var(--disc-shadow)"/>
      <circle cx="242" cy="494" r="91" fill="var(--disc)" stroke="var(--disc-rim)" stroke-width="5"/>
    </g>
    <g class="disc">
      <circle cx="628" cy="509" r="92" fill="var(--disc-shadow)"/>
      <circle cx="623" cy="502" r="91" fill="var(--disc)" stroke="var(--disc-rim)" stroke-width="5"/>
    </g>
    <g class="disc">
      <circle cx="248" cy="847" r="92" fill="var(--disc-shadow)"/>
      <circle cx="243" cy="840" r="91" fill="var(--disc)" stroke="var(--disc-rim)" stroke-width="5"/>
    </g>
    <g class="disc">
      <circle cx="628" cy="852" r="92" fill="var(--disc-shadow)"/>
      <circle cx="623" cy="845" r="91" fill="var(--disc)" stroke="var(--disc-rim)" stroke-width="5"/>
    </g>

    <!-- clock icon -->
    <g class="icon-clock" fill="none" stroke="var(--white)" stroke-linecap="round">
      <circle cx="241" cy="496" r="56" stroke-width="4.5"/>
      <g stroke-width="4.5">
        <path d="M241 447 V455"/><path d="M241 537 V545"/>
        <path d="M192 496 H200"/><path d="M282 496 H290"/>
        <path d="M206 461 L211 466"/><path d="M276 461 L271 466"/>
        <path d="M206 531 L211 526"/><path d="M276 531 L271 526"/>
      </g>
      <path d="M241 496 L215 479" stroke-width="5"/>
      <path d="M241 496 L274 474" stroke-width="5"/>
    </g>

    <!-- van icon -->
    <g class="icon-van" fill="none" stroke="var(--white)" stroke-width="3.5" stroke-linejoin="round">
      <path d="M559 522 V503 C559 496 565 492 572 490 L584 487 L601 466 C603 464 605 463 608 463 H680 C685 463 688 466 688 471 V517 C688 521 686 523 682 523 H669"/>
      <path d="M655 523 H586"/>
      <path d="M572 523 H562"/>
      <path d="M592 487 L605 471 H616 V487 Z"/>
      <circle cx="579" cy="519" r="7"/>
      <circle cx="662" cy="519" r="7"/>
      <path d="M573 544 H680" stroke-width="4"/>
    </g>

    <!-- washing machine icon -->
    <g class="icon-washer">
      <rect x="198" y="788" width="90" height="107" rx="4" fill="var(--white)"/>
      <rect x="198" y="800" width="90" height="3" fill="var(--disc)"/>
      <circle cx="211" cy="795" r="3" fill="var(--disc)"/>
      <circle cx="221" cy="795" r="3" fill="var(--disc)"/>
      <rect x="252" y="792" width="24" height="5" rx="2.5" fill="var(--disc)"/>
      <circle cx="243" cy="849" r="33" fill="var(--disc)"/>
      <circle cx="243" cy="849" r="29" fill="var(--white)"/>
      <path d="M214 843 Q221 849 228 843 Q235 849 243 843 Q250 849 257 843 Q264 849 272 843 A29 29 0 0 1 214 843 Z" fill="var(--disc)"/>
    </g>

    <!-- hanger icon -->
    <g class="icon-hanger">
      <path d="M614 800 C614 792 626 790 627 798 C628 804 620 805 620 812 V816 L574 848 C567 853 571 860 578 860 H666 C673 860 677 853 670 848 L620 816"
            fill="none" stroke="var(--white)" stroke-width="4" stroke-linecap="round" stroke-linejoin="round"/>
      <rect x="581" y="855" width="73" height="46" fill="var(--white)"/>
      <rect x="656" y="849" width="11" height="48" rx="3" fill="var(--white)"/>
      <path d="M662 856 V897" stroke="var(--disc)" stroke-width="2"/>
    </g>
  </svg>

  <p class="site-url">foldharborlaundry.example</p>
  <h1 class="headline">HOW IT WORKS</h1>

  <p class="step-text step-1">Schedule a pickup -<br>feel free to leave your<br>bag where our driver<br>can get to it.</p>
  <p class="step-text step-2">Our driver will<br>pickup your clothes<br>at the scheduled time.</p>
  <p class="step-text step-3">Your clothes are<br>expertly cleaned<br>by our team of<br>laundry professionals</p>
  <p class="step-text step-4">We delivery your<br>clean clothes<br>back to you at<br>your convenience!</p>

  <div class="footer-band"></div>
</main>
</body>
</html>
```